I need to redesign my landing page into a high converting landing page adding 3 new elements

I need to redesign my landing page using all the same content, images etc. on the current page https://www.brightlanepromoworks.biz/travel_agency but also adding three new elements to the new redesign.

Please be sure to use my current header and footer from my current website since I will just plug the new design into it...

The Three New Elements Are Below (add these 3 new elements in addition to the current content)

1. Add a video element with this content:
Watch Below To See How Your Industry Uses Our Incentives To Skyrocket Their Sales!

2. Add the element of the 6 types of incentives they can offer.
You can use the same content and images that we use in this module on the homepage at www.brightlanepromoworks.biz ATTACHED IMAGE BUT YOU CAN FIND THE ORIGINAL IMAGES ON HOMEPAGE

3. Add 1 more call to action to give website visitors two choices:
A. Sign Up For 14 Days Risk Free
OR
B. Book A Live Call

Target Market(s)

Travel agents and travel advisors

Industry/Entity Type

marketing

Requirements
Must have
• HIGH CONVERTING LANDING PAGE
Nice to have
• short and to the point...no fluff

```html
<!DOCTYPE html>
<html lang="en">
<head>
<meta charset="utf-8">
<title>Bright Lane Promo Works – Travel Agency Incentives</title>
<link href="https://fonts.googleapis.com/css2?family=Montserrat:wght@400;500;600;700;800&display=swap" rel="stylesheet">
<style>
:root{
  --navy:#2b2070;
  --title:#2d2a78;
  --blue:#2f78c4;
  --green:#22e61a;
  --lav:#f1effa;
  --text:#555a66;
  --dark:#1c2636;
  --white:#ffffff;
}
*{box-sizing:border-box;margin:0;padding:0}
html,body{width:1200px;height:4238px;overflow:hidden}
body{position:relative;font-family:'Montserrat',sans-serif;color:var(--text);background:var(--white)}
.abs{position:absolute}
a{color:inherit;text-decoration:none}

/* header */
.topbar{left:0;top:0;width:1200px;height:66px;background:#fff}
.brand{display:flex;align-items:center;gap:10px}
.brand-mark{width:34px;height:34px;background:var(--blue);border-radius:4px}
.brand-name{font-weight:700;color:var(--blue);font-size:17px;line-height:1.1;letter-spacing:.5px;text-transform:uppercase}
.top-actions{right:110px;top:20px;display:flex;gap:26px;font-size:13px;font-weight:700;color:var(--navy)}
.top-actions span{display:flex;align-items:center;gap:8px}
.ico-circ{width:24px;height:24px;border:2px solid var(--green);border-radius:50%}
.nav{left:0;top:66px;width:1200px;height:47px;background:var(--navy)}
.nav ul{list-style:none;display:flex;gap:22px;position:absolute;left:122px;top:15px;color:#fff;font-size:13px;font-weight:600}
.nav-cta{left:778px;top:0;width:312px;height:47px;background:var(--green);display:flex;justify-content:space-around;align-items:center;font-size:13px;font-weight:600;color:var(--navy)}

/* hero */
.hero{left:0;top:113px;width:1200px;height:420px;background:linear-gradient(180deg,#6c8aa0 0%,#3f7c7d 45%,#1f8d95 75%,#2a6f7a 100%)}
.hero h1{position:absolute;left:200px;width:800px;top:30px;text-align:center;color:#fff;font-size:47px;font-weight:700;line-height:52px;text-shadow:0 2px 6px rgba(0,0,0,.3)}
.btn{background:var(--green);color:var(--navy);font-weight:700;border-radius:22px;display:flex;align-items:center;justify-content:center;font-size:15px}
.hero-curve{left:0;top:400px;width:1200px;height:140px}

/* intro */
.intro{left:160px;top:575px;width:880px;text-align:center;font-size:23px;line-height:32px;color:#4a4f5a}
.intro strong{color:var(--title);font-weight:700}

/* video */
.video{left:222px;top:711px;width:756px;height:376px;border-radius:22px;background:linear-gradient(120deg,#6a86a8 0%,#c8d4e0 40%,#8ab0c8 70%,#d9b79a 100%);box-shadow:0 10px 30px rgba(40,40,90,.2)}
.play{left:347px;top:156px;width:60px;height:60px}
.video-cap{left:312px;top:1020px;width:576px;height:101px;background:#fff;border-radius:14px;box-shadow:0 8px 30px rgba(40,40,90,.18);text-align:center;padding-top:24px;font-size:18px;line-height:30px;color:#333}
.video-cap b{font-weight:700;color:#222}

/* sections */
.band{left:0;width:1200px}
.sec-title{position:absolute;left:0;width:1200px;text-align:center;color:var(--title);font-weight:800;font-size:34px;line-height:45px;text-transform:uppercase}
.sec-sub{position:absolute;left:220px;width:760px;text-align:center;font-size:15px;line-height:28px;color:#555}

/* helps */
.help{position:absolute;width:200px;text-align:center;font-size:16px;line-height:23px;color:#444}
.help .pic{width:172px;height:172px;border-radius:50%;margin:0 auto 20px;border:4px solid #fff;box-shadow:0 6px 18px rgba(40,40,90,.25)}

/* ad packs */
.pack{position:absolute;top:2004px;height:231px;background:#fff;border-radius:12px;box-shadow:0 4px 16px rgba(40,40,90,.15);border:1px solid #eceaf4}
.pack .flyer{position:absolute;top:40px;height:160px;border-radius:2px}
.dots{position:absolute;display:flex;gap:8px}
.dots i{display:block;width:18px;height:4px;border-radius:2px;background:#c7c3e0}
.dots i.on{width:40px;background:var(--title)}

/* testimonial */
.avatar{left:548px;top:2640px;width:104px;height:104px;border-radius:50%;background:radial-gradient(circle,#d08a5a,#8a4a30);border:5px solid #fff;box-shadow:0 4px 14px rgba(40,40,90,.2)}
.quote-mark{font-size:150px;font-weight:800;color:#9f9ad0;line-height:1;font-family:Georgia,serif}
.t-name{left:0;width:1200px;top:2762px;text-align:center;font-size:19px;font-weight:600;color:#333}
.stars{left:548px;top:2790px;width:104px;height:20px}
.t-text{left:250px;width:700px;top:2832px;text-align:center;font-size:15.5px;line-height:28.5px;color:#555}

/* incentive cards */
.inc{position:absolute;top:3380px;width:152px;text-align:center}
.inc .card{height:198px;border-radius:8px;box-shadow:0 4px 12px rgba(0,0,0,.2)}
.inc h3{margin-top:22px;font-size:14.5px;line-height:19px;font-weight:700;color:#333;text-transform:uppercase}
.inc p{font-size:13px;line-height:19px;color:#666}

/* footer */
.footer{left:0;top:3752px;width:1200px;height:486px;background:var(--dark);color:#d8dde6}
.f-brand{left:112px;top:78px;width:235px;text-align:center;color:var(--blue);font-weight:700;font-size:20px;line-height:24px;text-transform:uppercase}
.socials{left:140px;top:167px;display:flex;gap:12px}
.socials i{display:block;width:33px;height:33px;border-radius:50%;background:#4e5868}
.f-btn{left:113px;top:225px;width:232px;height:46px;font-size:12px;line-height:14px;text-align:center;border-radius:23px}
.f-col h4{font-size:15px;font-weight:800;color:#fff;text-transform:uppercase;letter-spacing:.5px;margin-bottom:18px}
.f-col li{list-style:none;font-size:11.5px;line-height:16px;margin-bottom:8px;color:#c9ceda}
.contact p{font-size:11.5px;line-height:16px;color:#c9ceda;padding-left:22px;position:relative;margin-bottom:8px}
.contact p b{color:#fff;font-weight:700}
.contact p em{font-style:normal;color:#f08a2c}
.contact svg{position:absolute;left:0;top:1px}
.copy{left:112px;top:455px;font-size:11.5px;color:#aab2c0}
.copy b{color:#fff}
.legal{right:110px;top:455px;font-size:11.5px;color:#aab2c0}
</style>
</head>
<body>

<!-- Header -->
<header class="abs topbar">
  <div class="abs brand" style="left:110px;top:14px">
    <div class="brand-mark"></div>
    <div class="brand-name">Bright Lane<br>Promo Works</div>
  </div>
  <div class="abs top-actions">
    <span><i class="ico-circ"></i>Login</span>
    <span><i class="ico-circ"></i>Sign Up</span>
  </div>
</header>
<nav class="abs nav">
  <ul>
    <li>Home</li><li>Incentives List</li><li>Get Free Samples</li><li>Integrations</li><li>Industries ▾</li>
  </ul>
  <div class="abs nav-cta"><span>Call or Text ▾</span><span>Book A Demo ▾</span></div>
</nav>

<!-- Hero -->
<section class="abs hero" role="img" aria-label="Traveller in a sun hat riding a longtail boat between limestone islands">
  <h1>Imagine Being Able To Offer BOGO Deals With Every Booking!</h1>
  <a class="abs btn" style="left:176px;top:222px;width:283px;height:43px">Sign Up For 14 Days Risk Free</a>
  <a class="abs btn" style="left:737px;top:222px;width:215px;height:43px">Book A Live Call</a>
</section>
<svg class="abs hero-curve" viewBox="0 0 1200 140" preserveAspectRatio="none">
  <path d="M0 25 Q600 175 1200 8 V140 H0Z" fill="#d9d4f2"/>
  <path d="M0 45 Q600 170 1200 30 V140 H0Z" fill="#ffffff"/>
</svg>

<!-- Intro -->
<p class="abs intro">Attract More New Customers Giving Away Free Vacation Certificates, Cruise Vouchers, Smart Devices, Dining Takeout Vouchers And More. <strong>You'll Never Pay For A Single Certificate,Vacation or Any Item, Ever.</strong></p>

<!-- Video -->
<div class="abs video" role="img" aria-label="Video preview: presenter in a suit over travel scenes">
  <svg class="abs play" viewBox="0 0 60 60"><circle cx="30" cy="30" r="27" fill="none" stroke="#fff" stroke-width="3"/><path d="M24 18 L42 30 L24 42Z" fill="#fff"/></svg>
</div>
<div class="abs video-cap">Watch To See How Your Industry Uses<br><b>Our Incentives To Skyrocket Their Sales!</b></div>

<!-- Help -->
<section class="abs band" style="top:1219px;height:538px;background:var(--lav)">
  <h2 class="sec-title" style="top:80px">Our Marketing Incentives<br>Can Help You With</h2>
  <div class="help" style="left:85px;top:214px"><div class="pic" role="img" aria-label="Swimmer in a blue sea cave" style="background:linear-gradient(160deg,#8aa4b0,#0f6f8c 60%,#0a8aa6)"></div>Special Promotion giveaway</div>
  <div class="help" style="left:292px;top:214px"><div class="pic" role="img" aria-label="Turquoise lagoon and tropical beach" style="background:linear-gradient(160deg,#b8d8e0,#3fc0c0 55%,#d8d0a0)"></div>Referral Gifts</div>
  <div class="help" style="left:498px;top:214px"><div class="pic" role="img" aria-label="Thatched beach huts under palm trees" style="background:linear-gradient(170deg,#6fa0d8,#e8eef2 45%,#6a7a50)"></div>Enticement for booking a flight</div>
  <div class="help" style="left:706px;top:214px"><div class="pic" role="img" aria-label="Pier over blue water with mountains" style="background:linear-gradient(180deg,#7fb2e8,#4a90c8 55%,#1a5a90)"></div>Gifts for booking a Cruise</div>
  <div class="help" style="left:912px;top:214px"><div class="pic" role="img" aria-label="Overwater villa interior" style="background:linear-gradient(160deg,#5a3a2a,#b08060 50%,#7ab8c8)"></div>Welcome Gifts</div>
</section>

<!-- Ad packs -->
<h2 class="sec-title" style="top:1825px">Plug-In-Play Ad Packs</h2>
<p class="sec-sub" style="top:1885px">Proven SocialFeed™ Ad Templates, High-Converting Banner Ad Templates To Use With The SearchGrid™ Display Network Plus Time-Tested Print Ad Templates That We Provide To You For Free With Your BLP Package.</p>
<div class="pack" style="left:-90px;width:444px">
  <div class="flyer" role="img" aria-label="Smart watch banner ad template" style="left:90px;width:110px;background:linear-gradient(180deg,#f3f3f3,#e8b890 60%,#2a4aa0)"></div>
  <div class="flyer" role="img" aria-label="Smart watch display ad template" style="left:215px;width:130px;background:linear-gradient(180deg,#fff,#e0c0a0 45%,#2a3a90)"></div>
</div>
<div class="pack" style="left:378px;width:443px">
  <div class="flyer" role="img" aria-label="Free 4 night cruise postcard template" style="left:28px;width:240px;background:linear-gradient(180deg,#3a2a70,#6a4a8a 50%,#c89050)"></div>
  <div class="flyer" role="img" aria-label="Free 4 night cruise flyer template" style="left:280px;width:122px;background:linear-gradient(180deg,#3a2a70,#6a4a8a 50%,#c89050)"></div>
</div>
<div class="pack" style="left:847px;width:443px">
  <div class="flyer" role="img" aria-label="4 night hotel stay postcard template" style="left:28px;width:240px;background:linear-gradient(180deg,#2a2040,#8a6040 55%,#d0a060)"></div>
  <div class="flyer" role="img" aria-label="4 night hotel stay flyer template" style="left:280px;width:122px;background:linear-gradient(180deg,#2a2040,#8a6040 55%,#d0a060)"></div>
</div>
<div class="dots" style="left:542px;top:2292px"><i class="on"></i><i></i><i></i><i></i></div>
<a class="abs btn" style="left:457px;top:2360px;width:285px;height:42px">Sign Up For 14 Days Risk Free</a>

<!-- Testimonials -->
<section class="abs band" style="top:2477px;height:655px;background:var(--lav)"></section>
<h2 class="sec-title" style="top:2557px">Client Testimonials</h2>
<div class="abs avatar" role="img" aria-label="Client portrait"></div>
<div class="abs quote-mark" style="left:158px;top:2735px">“</div>
<div class="abs quote-mark" style="left:980px;top:2920px">”</div>
<div class="abs t-name">Dana R.</div>
<svg class="abs stars" viewBox="0 0 104 20">
  <g fill="#f5b800">
    <path id="st" d="M10 1l2.6 6 6.4.5-4.9 4.2 1.5 6.3L10 14.7 4.4 18l1.5-6.3L1 7.5l6.4-.5z"/>
    <use href="#st" x="21"/><use href="#st" x="42"/><use href="#st" x="63"/><use href="#st" x="84"/>
  </g>
</svg>
<p class="abs t-text">I was so happy to hear from one of our clients who was thrilled after she redeemed her certificate for a four-night hotel stay. She got the date she wanted and the hotel she chose. She has two kids and she got a three-bedroom town house that sleeps six, only three miles from Sunny Park. They also had three pools and family activities. I have been with BLP for 8 months now and I have never had a complaint from any of our clients who redeem their certificates. It is the best deal out there.</p>
<div class="dots" style="left:542px;top:3045px"><i class="on"></i><i></i><i></i><i></i></div>

<!-- Incentives -->
<h2 class="sec-title" style="top:3215px">Incentives We Offer</h2>
<p class="sec-sub" style="top:3278px">Give Away An Unlimited Amount Of Complimentary Gift Vouchers Redeemable For:<br>(Without Having To Personally Fulfill Or Pay For Any Of Them Yourself!)</p>
<div class="inc" style="left:110px"><div class="card" role="img" aria-label="Hotel saving card certificate" style="background:linear-gradient(180deg,#f6f2ee,#e0b090 50%,#8a3a2a)"></div><h3>Hotel Saving Cards</h3><p>Complimentary<br><b>$100-$500</b><br>Hotel Cards</p></div>
<div class="inc" style="left:275px"><div class="card" role="img" aria-label="Smart device certificate" style="background:linear-gradient(180deg,#f8f2e6,#e8c880 50%,#a07a20)"></div><h3>Smart Device Certificates</h3><p>Complimentary<br>Smart Devices</p></div>
<div class="inc" style="left:440px"><div class="card" role="img" aria-label="Restaurant card certificate" style="background:linear-gradient(180deg,#f6f2ee,#d08070 50%,#6a1a1a)"></div><h3>Restaurant Cards</h3><p>Complimentary<br><b>$100-$500</b><br>Dining Cards</p></div>
<div class="inc" style="left:606px"><div class="card" role="img" aria-label="Airfare voucher" style="background:linear-gradient(180deg,#f6f2ee,#e09070 50%,#6a3a6a)"></div><h3>Airfare Voucher</h3><p>Complimentary<br>Roundtrip Airfare</p></div>
<div class="inc" style="left:771px"><div class="card" role="img" aria-label="Cruise certificate" style="background:linear-gradient(180deg,#f4f2f4,#80a8c8 50%,#5a4a7a)"></div><h3>Cruise Certificates</h3><p>Complimentary<br>Cruise Getaways</p></div>
<div class="inc" style="left:936px"><div class="card" role="img" aria-label="Resort certificate" style="background:linear-gradient(180deg,#f4f2f6,#a090c8 50%,#6a2a7a)"></div><h3>Resort Certificates</h3><p>Complimentary All<br>Inclusive Vacations</p></div>

<!-- Footer -->
<footer class="abs footer">
  <div class="abs f-brand">Bright Lane<br>Promo Works</div>
  <div class="abs socials"><i></i><i></i><i></i><i></i></div>
  <a class="abs btn f-btn">SIGN UP FOR A 14 DAY RISK<br>FREE TRIAL</a>

  <div class="abs f-col contact" style="left:388px;top:62px;width:275px">
    <h4>Contact Us</h4>
    <p><svg width="13" height="14" viewBox="0 0 13 14"><path d="M6.5 1a4.5 4.5 0 0 0-4.5 4.5C2 9 6.5 13 6.5 13S11 9 11 5.5A4.5 4.5 0 0 0 6.5 1z" fill="none" stroke="#c9ceda"/><circle cx="6.5" cy="5.5" r="1.5" fill="#c9ceda"/></svg><b>Bright Lane Promo Works Group, Inc.</b><br>2450 Harbor View Rd #310<br>Seaside Bay, CA 90000</p>
    <p><svg width="13" height="13" viewBox="0 0 13 13"><rect x="1" y="2" width="11" height="10" rx="1" fill="none" stroke="#c9ceda"/><path d="M1 5h11" stroke="#c9ceda"/></svg><b>Book A Demo:</b><br>New Sales<br>Current/Past Clients</p>
    <p><svg width="13" height="13" viewBox="0 0 13 13"><path d="M3 1l2 3-1.5 1.5a7 7 0 0 0 4 4L9 8l3 2-1 2C6 12 1 7 1 2z" fill="none" stroke="#c9ceda"/></svg><b>Call Or Text Us:</b><br>New Sales 1-555-210-4181<br>Current/Past Clients 1-555-340-9633</p>
    <p><svg width="13" height="11" viewBox="0 0 13 11"><rect x="1" y="1" width="11" height="9" fill="none" stroke="#c9ceda"/><path d="M1 1l5.5 5L12 1" fill="none" stroke="#c9ceda"/></svg>support@brightlanepromoworks.biz</p>
    <p><svg width="13" height="13" viewBox="0 0 13 13"><circle cx="6.5" cy="6.5" r="5.5" fill="none" stroke="#c9ceda"/><path d="M6.5 3v3.5l2.5 1.5" fill="none" stroke="#c9ceda"/></svg><b>SMS, Email &amp; Online Support:</b><br>Monday - Friday <em>8am - 5pm PST</em><br><em>Sat/Sun/Holidays Closed</em><br>*After Hours All Inquiries Will Be Replied To On The Next Business Day.</p>
  </div>

  <div class="abs f-col" style="left:705px;top:62px;width:150px">
    <h4>Quick Links</h4>
    <ul><li>Home</li><li>The Incentives</li><li>Login</li><li>Sign Up</li><li>Affiliate</li><li>Integrations</li><li>Testimonials</li><li>Frequently Asked Questions</li><li>BLP Distribute Certificate Demo Videos</li><li>White Label Agency Program</li></ul>
  </div>

  <div class="abs f-col" style="left:895px;top:62px;width:200px">
    <h4>Other Links</h4>
    <ul><li>Hoteliers</li><li>BLP Certificates List</li><li>How To Use BLP Certificates</li><li>Pop Ups &amp; Sticky Bars</li><li>Whitepaper - Increase Sales</li><li>Whitepaper - Improve Sales During Strange Times</li><li>Whitepaper - Boost Website Conversions</li></ul>
  </div>

  <div class="abs copy">© 2024 <b>Bright Lane Promo Works Group, Inc.</b> All Rights Reserved.</div>
  <div class="abs legal">Privacy Policy &nbsp;|&nbsp; Term And Conditions</div>
</footer>

</body>
</html>
```